Sudden Tides "Lantern Road" New Single Cover

Create cover artwork for the band Sudden Tides' new single "Lantern Road" being released early 2020. Style, font and graphics to be consistent with band's previous releases and overall brand identity. Visit www.suddentidesband.example and our Spotify page https://music.example.net/artist/7QzWpLx3RtVnKd8e2YbHcJ?si=MUrTgKa4PLe7skvWq2AmZd to view our previous releases and overall brand identity. Some examples attached as well. We are looking for someone to work with on future projects as well.

Lyrics are here: https://docs.example.org/document/d/3KTp9wrn_2ZQa8eXb4Lo_fimH7C5m83Jz4Pd70hrtVcA/edit

Music is here: https://audiostream.example.com/suddentides/lantern-road/s-pzkwa

Font styles to use
Sans Serif

Colors

Designer to choose colors to be used in the design.

Requirements
Must have
• Must be consistent with current brand identity and with prior album / single art.

```html
<!DOCTYPE html>
<html lang="en">
<head>
<meta charset="utf-8">
<title>Sudden Tides – Lantern Road</title>
<link href="https://fonts.googleapis.com/css2?family=Josefin+Sans:wght@400;700&display=swap" rel="stylesheet">
<style>
  :root {
    --sun-pale: #fde9a6;
    --sun-gold: #fdc814;
    --sun-deep: #f6a21e;
    --ink-navy: #1f2a5c;
    --sage-glow: rgba(159, 191, 138, 0.55);
    --frame-white: rgba(255, 255, 255, 0.6);
  }
  html, body {
    margin: 0;
    padding: 0;
    width: 1200px;
    height: 1200px;
    overflow: hidden;
    background: #ffffff;
  }
  .cover {
    position: relative;
    width: 1200px;
    height: 1200px;
    overflow: hidden;
    background: linear-gradient(90deg, var(--sun-pale) 0%, var(--sun-gold) 38%, var(--sun-gold) 62%, var(--sun-deep) 100%);
    font-family: "Josefin Sans", sans-serif;
  }
  .inner-frame {
    position: absolute;
    left: 62px;
    top: 62px;
    width: 1076px;
    height: 1076px;
    box-sizing: border-box;
    border: 1.5px solid var(--frame-white);
  }
  .centre-motif {
    position: absolute;
    left: 190px;
    top: 200px;
    width: 820px;
    height: 790px;
    border-radius: 50%;
    background: radial-gradient(closest-side, var(--sage-glow) 0%, rgba(159, 191, 138, 0.25) 60%, rgba(159, 191, 138, 0) 100%);
  }
  .single-title {
    position: absolute;
    left: 0;
    right: 0;
    top: 372px;
    margin: 0;
    text-align: center;
    color: var(--ink-navy);
    font-family: "Josefin Sans", sans-serif;
    font-weight: 400;
    line-height: 1;
    text-transform: uppercase;
  }
  .single-title-top {
    display: block;
    font-size: 200px;
    letter-spacing: 2px;
  }
  .single-title-bottom {
    display: block;
    margin-top: 28px;
    font-size: 250px;
    letter-spacing: 4px;
  }
  .band-name {
    position: absolute;
    right: 114px;
    bottom: 112px;
    margin: 0;
    font-family: "Josefin Sans", sans-serif;
    font-weight: 700;
    font-size: 42px;
    line-height: 1;
    letter-spacing: 1px;
    color: var(--ink-navy);
    text-transform: uppercase;
  }
</style>
</head>
<body>
  <main class="cover">
    <div class="centre-motif" role="img" aria-label="Soft sage heart motif behind the title"></div>
    <div class="inner-frame" aria-hidden="true"></div>

    <h1 class="single-title">
      <span class="single-title-top">Lantern</span>
      <span class="single-title-bottom">Road</span>
    </h1>

    <p class="band-name">Sudden Tides</p>
  </main>
</body>
</html>
```